Flyer for rhytmic gymnastics school

Hello everybody. We are planning to launch advertising campaign for our rhytmic gymnastics school. The flyers will be distributed directly to people throughout the city putting them on doorknobs. So the design should be very attractive and clear. Our goal is to attract small girls age 3-5. The idea and concept of the flyer is up to you but we just want to empasize the attractivness and benefits of this sport - basically it's a combination of ballet, gymnastics and dance. We even consider using cartoonish style of the flyer. We also have our logo, it's attached. The school is located in Southern California, with a diverse population. Chinese and Korean families that recently came to the US probably will be the main target audience since they know about this sport more. So one the goals is to show people who have never heard about Rhytmic Gymnastics what this sport is about. We need to design both sides of the flyers. We think that on one side of the flyer should be placed photo of our school (it should be ready in two days) and information about facility, adress etc. And as I mentioned one side should be creative and unusual to attract kids and parents. Here is some information about VP in general

Looking for new sport for your daughter?
Try Rhythmic Gymnastics! It’s an Olympic Sport!

• Enrollment is now open for Girls 3, 5-5 year old
• Competitive opportunity or recreational classes
• Instruction based on Russian School of Rhythmic Gymnastics
• A team of professional coaches
Brand new facility exlusively for rhytmic gymnastics activity
FREE introductory class!

Rhythmic Gymnastics is a discipline combining grace, coordination, agility and
artistry.
Rhythmic gymnastics combines ballet and creative movements to music, while
working with ribbons, balls, hoops, ropes and clubs in a choreographed danceand-tumble routine. Rhythmic gymnastics creates beautiful strong bodies as well
as improving child’s cognitive abilities

Requirements
Must have
• We see the flyer as a double sided flat A6 size, but again it's up to you.
Location
41876 Marlow Crest dr
Laguna Hills, CA
92653
www.vendapoise.us
Phone # 555 382 4106
e-mail kids@vendapoise.us
Facebook page https://www.facebook.com/TolvaRhythmicGymnastics

```html
<!DOCTYPE html>
<html lang="en">
<head>
<meta charset="utf-8">
<title>Tolva School of Rhythmic Gymnastics – Flyer</title>
<link rel="stylesheet" href="https://fonts.googleapis.com/css2?family=Shadows+Into+Light+Two&family=Lato:wght@700&display=swap">
<style>
  :root {
    --ink: #2b1620;
    --plum: #7a1452;
    --magenta: #c23386;
    --rose: #e59bc7;
    --blush: #f6dcea;
    --white: #ffffff;
    --hand: "Shadows Into Light Two", cursive;
    --sans: "Lato", sans-serif;
  }
  * { margin: 0; padding: 0; box-sizing: border-box; }
  html, body { width: 843px; height: 1200px; overflow: hidden; background: var(--white); }
  .flyer {
    position: relative;
    width: 843px;
    height: 1200px;
    overflow: hidden;
    background: linear-gradient(180deg, var(--white) 0%, var(--blush) 25%, var(--rose) 58%, var(--magenta) 84%, var(--plum) 100%);
    font-family: var(--hand);
    color: var(--ink);
  }
  .glow {
    position: absolute;
    inset: 0;
    background: radial-gradient(ellipse 55% 45% at 62% 68%, rgba(255,255,255,0.35) 0%, rgba(255,255,255,0) 70%);
  }
  .gymnast {
    position: absolute;
    left: 285px;
    top: 110px;
    width: 220px;
    height: 1090px;
    border-radius: 110px 110px 50px 50px;
    background: radial-gradient(ellipse at 50% 40%, rgba(255,255,255,0.55) 0%, rgba(226,140,196,0.4) 45%, rgba(160,40,110,0) 75%);
  }
  .brand {
    position: absolute;
    left: 0;
    top: 52px;
    width: 128px;
    height: 132px;
    background: var(--white);
    display: flex;
    flex-direction: column;
    justify-content: center;
    padding-left: 10px;
    font-family: var(--sans);
    font-weight: 700;
    color: var(--plum);
  }
  .brand-name { font-size: 26px; letter-spacing: 1px; line-height: 1; }
  .brand-sub { font-size: 12px; line-height: 1.2; margin-top: 6px; }
  .brand-mark {
    position: absolute;
    left: 146px;
    top: 78px;
    width: 60px;
    height: 60px;
    border-radius: 50%;
    background: var(--magenta);
    opacity: 0.85;
  }
  .headline {
    position: absolute;
    left: 0;
    top: 212px;
    width: 100%;
    text-align: center;
    font-weight: 400;
    font-size: 33px;
    line-height: 1.35;
  }
  .about {
    position: absolute;
    left: 90px;
    top: 418px;
    width: 663px;
    text-align: center;
    font-size: 23px;
    line-height: 1.42;
  }
  .benefits {
    position: absolute;
    left: 22px;
    top: 895px;
    width: 780px;
    list-style: none;
    font-size: 24px;
    line-height: 1.38;
    color: var(--ink);
  }
  .benefits li.dot::before { content: "•"; margin-right: 10px; }
</style>
</head>
<body>
<main class="flyer">
  <div class="glow" aria-hidden="true"></div>

  <div class="gymnast" role="img" aria-label="Silhouette of a rhythmic gymnast in a standing split, glowing pink"></div>

  <div class="brand">
    <span class="brand-name">TOLVA</span>
    <span class="brand-sub">School of<br>Rhythmic<br>Gymnastics</span>
  </div>
  <span class="brand-mark" aria-hidden="true"></span>

  <h1 class="headline">Looking for new sport for your daughter?<br>Try Rhythmic Gymnastics! It's an Olympic Sport</h1>

  <p class="about">Rhythmic Gymnastics is a discipline combining grace,<br>coordination, agility andartistry.<br>Rhythmic gymnastics combines ballet and creative movements to music, whileworking with ribbons, balls, hoops, ropes and clubs in a choreographed danceand-tumble routine. Rhythmic gymnastics creates beautiful strong bodies as wellas improving child's cognitive abilities</p>

  <ul class="benefits">
    <li class="dot">Enrollment is now open for Girls 3, 5-5 year old</li>
    <li class="dot">Competitive opportunity or recreational classes</li>
    <li class="dot">Instruction based on Russian School of Rhythmic Gymnastics</li>
    <li class="dot">A team of professional coaches</li>
    <li>Brand new facility exlusively for rhytmic gymnastics activity</li>
    <li>FREE introductory class</li>
  </ul>
</main>
</body>
</html>
```